Company Brochure / Data Sheet Template Design

We need a brochure / data sheet template for a new company based in Texas focused on Information Technology consulting. The design should instill professionalism, confidence, and strength. The company name is Brightwell Systems Partners, so you can incorporate alchemy concept into the design. I have attached the logo for the company. Our customers are medium and large businesses. We would like the top bar to incorporate black background to complement the black logo. Alternatively, you can incorporate the blue color and the white logo.

We will use this template for all corporate market materials. It should be usable for 1-6 pages documents.

Below are a couple examples by large technology companies:
http://www.korvanta.com/files/pdf/products/nimbrel/Korvanta-Nimbrel-zRAQ-Pricing-FAQs.pdf
https://www.peltrox.com/content/dam/peltrox/en_us/documents/products-solutions/the-peltrox-advantage-for-quillos-10.pdf

Please let us know if you have any questions.

Target Market(s)

Large Corporations and Small-to-Medium sized businesses

Industry/Entity Type

Information Technology

Font styles to use
Other font styles liked:
• Copperplate Gothic or something similar to the logo design

Requirements
Must have
• Design on the top of the page cover cross the entire page. Incorporate www.brightwellsyspartners.com or logo at the bottom of the page. Incorporate page numbers at the bottom of the page. Template should have the ability to incorporate 1 or 2 columns of content.
• This should match the look and feel of the logo.
Nice to have
• Template should have the ability to incorporate 1 or 2 columns of content
• Incorporate font and blue color into the design.
• Blue color could be incorporated into the headings of the content
Should not have
• This needs to be professional, not playful.

```html
<!DOCTYPE html>
<html lang="en">
<head>
<meta charset="utf-8">
<title>Brightwell Systems Partners – Data Sheet</title>
<link rel="stylesheet" href="https://fonts.googleapis.com/css2?family=Lato:wght@300;400&display=swap">
<style>
  :root {
    --backdrop: #d6d6d6;
    --page: #000000;
    --accent: #1ea4ba;
    --text: #f2f2f2;
    --rule: #ffffff;
    --rule-soft: #bdbdbd;
    --muted: #c4c4c4;
  }
  * { box-sizing: border-box; margin: 0; padding: 0; }
  html, body {
    width: 1058px;
    height: 1200px;
    overflow: hidden;
    background: var(--backdrop);
    font-family: "Lato", Arial, sans-serif;
  }
  .sheet {
    position: absolute;
    left: 65px;
    top: 0;
    width: 927px;
    height: 1200px;
    background: var(--page);
    color: var(--text);
  }
  .masthead {
    position: absolute;
    top: 48px;
    left: 0;
    width: 100%;
    display: flex;
    flex-direction: column;
    align-items: center;
  }
  .brand-mark {
    width: 92px;
    height: 92px;
  }
  .brand-name {
    margin-top: 22px;
    font-weight: 300;
    font-size: 27px;
    letter-spacing: 3px;
    text-transform: uppercase;
    color: var(--text);
  }
  .header-rule {
    position: absolute;
    top: 244px;
    left: 60px;
    width: 806px;
    height: 4px;
    background: var(--rule);
  }
  .columns {
    position: absolute;
    top: 280px;
    left: 61px;
    width: 806px;
    display: flex;
    justify-content: space-between;
  }
  .column { width: 372px; }
  .article { margin-bottom: 44px; }
  .article h2 {
    font-weight: 400;
    font-size: 24px;
    line-height: 24.5px;
    color: var(--accent);
    margin-bottom: 22px;
  }
  .article p {
    font-weight: 400;
    font-size: 17px;
    line-height: 18px;
    color: var(--text);
  }
  .article p + p { margin-top: 18px; }
  .footer-rule {
    position: absolute;
    top: 1114px;
    left: 60px;
    width: 806px;
    height: 2px;
    background: var(--rule-soft);
  }
  .site-url {
    position: absolute;
    top: 1126px;
    left: 0;
    width: 100%;
    text-align: center;
    font-weight: 300;
    font-size: 20px;
    color: var(--muted);
  }
  .page-number {
    position: absolute;
    top: 1158px;
    left: 0;
    width: 100%;
    text-align: center;
    font-size: 17px;
    color: var(--accent);
  }
</style>
</head>
<body>
<main class="sheet">
  <header class="masthead">
    <svg class="brand-mark" viewBox="0 0 92 92" aria-hidden="true">
      <circle cx="46" cy="46" r="40" fill="none" stroke="var(--accent)" stroke-width="9"/>
    </svg>
    <div class="brand-name">Brightwell Systems Partners</div>
  </header>
  <div class="header-rule"></div>

  <section class="columns">
    <div class="column">
      <article class="article">
        <h2>Verdanix enters Asia-Pacific market, dedicates itself to make strategic investments</h2>
        <p>Software provider, Verdanix, has expanded its operations to the Asia-Pacific region with the appointment of a new regional head, Dana Whitlock.</p>
      </article>
      <article class="article">
        <h2>Verdanix enters Asia-Pacific market, dedicates itself to make strategic investments</h2>
        <p>Software provider, Verdanix, has expanded its operations to the Asia-Pacific region with the appointment of a new regional head, Dana Whitlock.</p>
        <p>Whitlock will be based at the company’s new Asia-Pacific regional office in Melbourne and will be responsible for driving revenue and overseeing sales and channel development teams in the region.</p>
      </article>
      <article class="article">
        <h2>Verdanix enters Asia-Pacific market, dedicates itself to make strategic investments</h2>
        <p>Software provider, Verdanix, has expanded its operations to the Asia-Pacific region with the appointment of a new regional head, Dana Whitlock.</p>
        <p>Whitlock will be based at the company’s new Asia-Pacific regional office in Melbourne and will be responsible for driving revenue and overseeing sales and channel development teams in the region.</p>
      </article>
    </div>
    <div class="column">
      <article class="article">
        <h2>Verdanix enters Asia-Pacific market, dedicates itself to make strategic investments</h2>
        <p>Software provider, Verdanix, has expanded its operations to the Asia-Pacific region with the appointment of a new regional head, Dana Whitlock.</p>
        <p>Whitlock will be based at the company’s new Asia-Pacific regional office in Melbourne and will be responsible for driving revenue and overseeing sales and channel development teams in the region.</p>
      </article>
      <article class="article">
        <h2>Verdanix enters Asia-Pacific market, dedicates itself to make strategic investments</h2>
        <p>Software provider, Verdanix, has expanded its operations to the Asia-Pacific region with the appointment of a new regional head, Dana Whitlock.</p>
      </article>
      <article class="article">
        <h2>Verdanix enters Asia-Pacific market, dedicates itself to make strategic investments</h2>
        <p>Software provider, Verdanix, has expanded its operations to the Asia-Pacific region with the appointment of a new regional head, Dana Whitlock.</p>
        <p>Whitlock will be based at the company’s new Asia-Pacific regional office in Melbourne and will be responsible for driving revenue and overseeing sales and channel development teams in the region.</p>
      </article>
    </div>
  </section>

  <footer>
    <div class="footer-rule"></div>
    <div class="site-url">www.brightwellsyspartners.com</div>
    <div class="page-number">1</div>
  </footer>
</main>
</body>
</html>
```